Art Wall - Illustrates "Be Colorful"

I have a seasonal color business called Porch Step Blooms. We plant containers and add colorful annuals to garden beds. I need a 6' tall by 18' long banner that will be hung on a wall or possibly used on the side of my enclosed trailer. The banner will be used as backdrop for ladies taking pictures together and as a backdrop for colorful container gardens to be photographed for our website. It should have the words "Be Colorful" on it. I would like for it to look like a fun art wall that you would take a picture in front of in a downtown area. The art should work well with our logo. We love flowers but other ideas are welcome. Feel free to look at our instagram @porchstepbloomsokc to see examples of our work. I have uploaded our logo and a colorful flower picture we liked (great colors) but didn't quite work with our logo and a fun colorful wall at a restaurant that we really like.

Target Market(s)

women ages 30-45, wealthy, like to feel like they are trendy

Industry/Entity Type

Landscape Gardening

Font styles to use
Serif

Requirements
Must have
• The words "Be Colorful" on it and some space that would good for people to stand or objects to be placed to be photographed.
Nice to have
• We really like the colors in the "sun's out now" t-shirt picture I have attached. Also like the watercolor, alcohol ink, or hand-painted look.
Should not have
• Please do not include our logo on the banner. It will be added as a watermark to our photos.

Please do not literally use the logo flower in the design. Feel free to use pieces or inspiration from the logo but the wall should look more like art and less like a cartoon.

```html
<!DOCTYPE html>
<html lang="en">
<head>
<meta charset="utf-8">
<title>Be Colorful – Art Wall Banner</title>
<link rel="stylesheet" href="https://fonts.googleapis.com/css2?family=Noto+Serif:wght@700&display=swap">
<style>
  :root {
    --violet: #c58be0;
    --lilac: #e7a6dc;
    --pink: #ef5f86;
    --red: #ee3f5a;
    --orange: #f8944a;
    --yellow: #fcc235;
    --gold: #f7b928;
    --lime: #b5d553;
    --green: #8ec63f;
    --teal: #6fc3b0;
    --blue: #3a9fe0;
    --indigo: #4e6fcf;
    --headline: #ffffff;
    --headline-glow: rgba(120, 70, 0, 0.55);
  }

  html, body {
    margin: 0;
    padding: 0;
    width: 1200px;
    height: 400px;
    overflow: hidden;
    background: #ffffff;
  }

  .banner {
    position: relative;
    width: 1200px;
    height: 400px;
    overflow: hidden;
  }

  .banner__artwork {
    position: absolute;
    inset: 0;
    background: radial-gradient(
      circle at 1300px 820px,
      var(--indigo) 0px,
      var(--blue) 250px,
      var(--blue) 420px,
      var(--teal) 500px,
      var(--green) 600px,
      var(--lime) 760px,
      var(--gold) 880px,
      var(--yellow) 980px,
      var(--orange) 1110px,
      var(--red) 1230px,
      var(--pink) 1320px,
      var(--lilac) 1430px,
      var(--violet) 1560px
    );
  }

  .banner__headline {
    position: absolute;
    top: 18px;
    right: 30px;
    margin: 0;
    font-family: "Noto Serif", Georgia, serif;
    font-weight: 700;
    font-size: 74px;
    line-height: 1.2;
    letter-spacing: 0.5px;
    color: var(--headline);
    text-transform: uppercase;
    text-shadow: 0 0 18px var(--headline-glow), 0 2px 6px var(--headline-glow);
    white-space: nowrap;
  }
</style>
</head>
<body>
  <main class="banner">
    <div class="banner__artwork" role="img" aria-label="Hand-coloured pencil rainbow sweeping in broad arcs from violet and pink through red, orange, yellow and green to blue"></div>
    <h1 class="banner__headline">Be Colorful</h1>
  </main>
</body>
</html>
```